4x6 Postcard Design Full Color Double Sided

Hello, I am in need of a postcard design. The document with details is attached. And I am writing here also:

To My Dear Colleague,

This week, I want you to do yourself and me a favor, okay?

I want you to ask your boss for a $100,000 per year salary increase. If the answer is no then I want you to “give yourself” a

$10,000 per month pay increase RIGHT NOW!

The opportunity to make 6-7 figures using SIMPLE online systems is exploding right before your eyes. Why aren’t you paying attention? Is It because you don’t have any idea how to earn money online? Or are you intimidated by the thought of it because you’re not tech-savvy?

Throw any negative thoughts out of your mind and let us help you build a $100,000 + yearly income that runs on automatic. We’re not promising a million dollars overnight or that you’ll be able to quit your job tomorrow, BUT if an extra $10,000 per month would help you reach your goals, then you should take action today!

OUR SIMPLE IS SO EASY TO USE, A FIFTH GRADER COULD BE SUCCESSFUL!

We’re so sure you will be successful with our system that we are inviting you to
GET STARTED TODAY FOR FREE!!!

That’s right…for FREE! No credit card is required.

GO SIGN UP NOW:
www.qmvhub.com/joinFREE
Enter Referral ID#

KV-R8057

Free offer expires in 48 hours!!!

Instructions for designers:
I’d like the color scheme to stay consistent with my company’s color scheme. To see the color scheme of Blue Lark Gains go to www.qmvhub.com
As you are reading the text, please make certain parts of the text be emphasized on the postcard – wherever you feel necessary. When you read it, what would catch your attention? Those parts are the parts I’d like you to emphasize on the card by making them bolder, or a different color, or larger or highlighted.

The postcard is a 4x6 card, double-sided, full color

The text above is for the front side. The back will be the same thing, except in the spot where I have KV-R8057. On the backside it should say: (Use ID# on reverse side)

It’s like you are really only designing a one-sided card because the back side is almost an exact duplicate.

Thank you, you rock! =)

Target Market(s)

work from home seekers / make money online enthusiasts

Font styles to use
Serif

Requirements
Must have
• Color scheme similar to the color scheme at www.qmvhub.com
• The rest of the requirements are attached to the word doc.
• I will also send the logo, but it wouldn't let me upload because the file is too large.
Nice to have
• I really I am looking for something that really looks clean, but attention-grabbing

```html
<!DOCTYPE html>
<html lang="en">
<head>
<meta charset="utf-8">
<title>Blue Lark Gains – Postcard, front and back</title>
<link rel="stylesheet" href="https://fonts.googleapis.com/css2?family=Questrial&family=Montserrat:wght@700;800&family=Oswald:wght@400;500&display=swap">
<style>
  :root {
    --page: #ececec;
    --sky-top: #7fc6e4;
    --sky-mid: #bfe3f1;
    --haze: #9fb9c4;
    --rock: #7d7468;
    --panel: rgba(240, 240, 238, 0.96);
    --ink: #2b2b2b;
    --red: #e3191f;
    --black: #1d1d1d;
    --logo-ink: #4a4d52;
    --logo-ring: #3ea9dc;
    --white: #ffffff;
  }
  * { box-sizing: border-box; margin: 0; padding: 0; }
  html, body { width: 830px; height: 1200px; overflow: hidden; }
  body { background: var(--page); font-family: "Questrial", sans-serif; color: var(--ink); position: relative; }

  .postcard {
    position: absolute; left: 99px; width: 633px; height: 487px;
    background: var(--white);
    box-shadow: 0 3px 8px rgba(0,0,0,0.35);
    overflow: hidden;
  }
  .postcard--front { top: 84px; }
  .postcard--back { top: 629px; }

  .scene {
    position: absolute; inset: 0;
    background:
      linear-gradient(160deg, transparent 55%, rgba(125,116,104,0.9) 70%, var(--rock) 100%),
      linear-gradient(180deg, var(--sky-top) 0%, var(--sky-mid) 45%, var(--haze) 75%, #8a8478 100%);
  }
  .postcard--back .scene {
    clip-path: polygon(0 0, 476px 0, 476px 151px, 306px 151px, 306px 406px, 75px 406px, 75px 487px, 0 487px);
  }

  .panel { position: absolute; background: var(--panel); border-radius: 16px; }
  .postcard--front .panel { left: 17px; top: 32px; width: 412px; height: 430px; }
  .postcard--back .panel { left: 21px; top: 16px; width: 267px; height: 297px; }

  .panel > * { position: absolute; }
  .postcard--front .panel > p { left: 14px; width: 380px; }
  .postcard--back .panel > p { left: 10px; width: 247px; }

  .greeting { font-size: 22px; line-height: 26px; }
  .copy { font-size: 14.2px; line-height: 19px; }
  .copy--justify { text-align: justify; }
  .postcard--back .copy { font-size: 11px; line-height: 14.6px; }

  .shout {
    font-family: "Montserrat", sans-serif; font-weight: 800; color: var(--red);
    font-size: 14.2px; line-height: 19px; text-transform: uppercase;
  }
  .postcard--back .shout { font-size: 10.4px; line-height: 14.4px; white-space: nowrap; }
  .free { font-family: "Montserrat", sans-serif; font-weight: 800; color: var(--red); }

  .price-badge {
    display: flex; align-items: center;
    width: 226px; height: 44px;
    background: var(--red); border-radius: 5px;
    outline: 1px dashed rgba(255,255,255,0.85); outline-offset: -4px;
    box-shadow: 0 12px 8px -8px rgba(0,0,0,0.45);
    color: var(--white); font-family: "Oswald", sans-serif; white-space: nowrap; overflow: hidden;
  }
  .price-badge__amount { font-size: 28px; font-weight: 500; padding: 0 6px 0 10px; border-right: 2px solid var(--white); line-height: 32px; }
  .price-badge__text { padding-left: 5px; }
  .price-badge__small { font-size: 11.5px; font-weight: 400; display: block; line-height: 14px; }
  .price-badge__big { font-family: "Montserrat", sans-serif; font-weight: 800; font-size: 15px; display: block; line-height: 17px; }

  .brand {
    position: absolute; background: rgba(255,255,255,0.9);
    display: flex; align-items: center; justify-content: center; gap: 8px;
  }
  .postcard--front .brand { left: 429px; top: 42px; width: 204px; height: 65px; }
  .postcard--back .brand { left: 288px; top: 16px; width: 188px; height: 59px; }
  .brand__mark { width: 20px; height: 20px; border-radius: 50%; border: 3px solid var(--logo-ring); }
  .brand__name { font-size: 21px; color: var(--logo-ink); }

  .signup {
    position: absolute; background: var(--white); border-radius: 6px;
    border: 1.5px dashed var(--black); text-align: center;
    box-shadow: 0 12px 8px -8px rgba(0,0,0,0.5);
  }
  .postcard--front .signup { left: 439px; top: 162px; width: 176px; height: 80px; }
  .postcard--back .signup { left: 71px; top: 319px; width: 167px; height: 80px; }
  .signup__head {
    background: var(--black); color: var(--white); border-radius: 5px 5px 0 0;
    font-family: "Montserrat", sans-serif; font-weight: 700; font-size: 14.5px; line-height: 20px;
  }
  .signup__url { font-size: 11px; margin-top: 3px; }
  .signup__id { font-family: "Oswald", sans-serif; font-size: 12.5px; margin-top: 4px; }
  .signup__expires { font-family: "Montserrat", sans-serif; font-weight: 700; font-size: 9.4px; margin-top: 5px; white-space: nowrap; }

  .arrow { position: absolute; left: 0; top: 0; pointer-events: none; }
</style>
</head>
<body>

<section class="postcard postcard--front">
  <div class="scene" role="img" aria-label="Photo of a climber scaling a rocky cliff above misty blue mountains under a bright sky"></div>

  <div class="panel">
    <p class="greeting" style="top:15px">To My Dear Colleague,</p>
    <p class="copy" style="top:48px">This week, I want you to do yourself and me a favor, okay?</p>
    <p class="copy" style="top:70px">I want you to ask your boss for a $100,000 per year<br>salary increase. If the answer is no then I want you to<br>“give yourself” a</p>
    <div class="price-badge" style="left:87px; top:140px">
      <span class="price-badge__amount">$10,000</span>
      <span class="price-badge__text"><span class="price-badge__small">Per Month Pay Increase</span><span class="price-badge__big">RIGHT NOW!</span></span>
    </div>
    <p class="copy copy--justify" style="top:192px">The opportunity to make 6-7 figures using SIMPLE online systems is exploding right before your eyes. Why aren't you paying attention? Is It because you don't have any idea how to earn money online? Or are you intimidated by the thought of it because you're not tech-savvy?</p>
    <p class="shout" style="top:291px">Our simple system is so easy to use, a fifth grader could be successful!</p>
    <p class="copy" style="top:332px">We're so sure you will be successful with our system that we are inviting you to</p>
    <p class="shout" style="top:376px">Get started today for free!!!</p>
    <p class="copy" style="top:398px">That's right…for <span class="free">FREE!</span> No credit card is required.</p>
  </div>

  <svg class="arrow" width="633" height="487" viewBox="0 0 633 487" aria-hidden="true">
    <path d="M146 150 H 384 Q 396 150 396 162 V 184 Q 396 196 384 196 H 342" fill="none" stroke="#e3191f" stroke-width="1.6" stroke-dasharray="7 5"/>
    <path d="M336 196 l8 -4 v8 z" fill="#e3191f"/>
  </svg>

  <div class="brand">
    <span class="brand__mark"></span>
    <span class="brand__name">Blue Lark Gains</span>
  </div>

  <div class="signup">
    <div class="signup__head">GO SIGN UP NOW</div>
    <div class="signup__url">www.qmvhub.com/joinFREE</div>
    <div class="signup__id">Use ID# on reverse side</div>
    <div class="signup__expires">Free offer expires in 48 hours!!!</div>
  </div>
</section>

<section class="postcard postcard--back">
  <div class="scene" role="img" aria-label="Photo of sky and a climber on a rocky cliff face"></div>

  <div class="panel">
    <div class="price-badge" style="left:24px; top:14px; width:225px">
      <span class="price-badge__amount">$10,000</span>
      <span class="price-badge__text"><span class="price-badge__small">Per Month Pay Increase</span><span class="price-badge__big">RIGHT NOW!</span></span>
    </div>
    <p class="copy copy--justify" style="top:70px">Let us help you build a $100,000 + yearly income that runs on automatic. We're not promising a million dollars overnight or that you'll be able to quit your job tomorrow, BUT if an extra $10,000 per month would help you reach your goals, then you should take action today!</p>
    <p class="shout" style="top:170px">Our simple system is so easy to use,<br>a fifth grader could be successful!</p>
    <p class="copy" style="top:208px">We're so sure you will be successful with our<br>system that we are inviting you to</p>
    <p class="shout" style="top:248px">Get started today for free!!!</p>
    <p class="copy" style="top:271px">That's right…for <span class="free">FREE!</span> No credit card is required.</p>
  </div>

  <div class="brand">
    <span class="brand__mark"></span>
    <span class="brand__name" style="font-size:19px">Blue Lark Gains</span>
  </div>

  <div class="signup">
    <div class="signup__head">GO SIGN UP NOW</div>
    <div class="signup__url">www.qmvhub.com/joinFREE</div>
    <div class="signup__id">Referral ID# KV-R8057</div>
    <div class="signup__expires">Free offer expires in 48 hours!!!</div>
  </div>
</section>

</body>
</html>
```